Brightkeel Logistics - Cards and Logo

We need a logo and card design for a Logistics company located in Chicago. Our competitors are KTR and Qorvan. We would like to see designs that incorporate a logo that shows all ways in terms of direction. The colors would be Electric Blue, Grays, Blacks and White. I like how Moko has a badge type logo that is strong and clean. Velmora also has a strong font that is futuristic. The final design should communicate we are a strong and technological type of company. I show a picture of the colors we like from a moko cooler.

```html
<!DOCTYPE html>
<html lang="en">
<head>
<meta charset="utf-8">
<title>Brightkeel Logistics – Business Card</title>
<link rel="stylesheet" href="https://fonts.googleapis.com/css2?family=Lato:wght@400;700;900&display=swap">
<style>
  :root {
    --navy: #0b3a72;
    --gray: #7a7a7a;
    --ink: #1e1e1e;
    --paper: #ffffff;
    --backdrop: #e4e6e9;
  }
  * { box-sizing: border-box; margin: 0; padding: 0; }
  html, body { width: 1200px; height: 782px; overflow: hidden; }
  body {
    background: var(--backdrop);
    font-family: "Lato", sans-serif;
    display: flex;
    align-items: center;
    justify-content: center;
    gap: 40px;
  }
  .card {
    position: relative;
    width: 540px;
    height: 309px;
    overflow: hidden;
    box-shadow: 0 6px 18px rgba(0,0,0,.18);
  }
  .card--front { background: var(--paper); }
  .card--back {
    background: var(--navy);
    display: flex;
    align-items: center;
    justify-content: center;
  }

  .holder { position: absolute; left: 34px; top: 28px; }
  .holder__name {
    font-weight: 900;
    font-size: 17px;
    letter-spacing: .5px;
    color: var(--navy);
    text-transform: uppercase;
  }
  .holder__role { font-size: 12px; color: var(--ink); margin-top: 1px; }

  .contact {
    position: absolute;
    left: 34px;
    top: 90px;
    list-style: none;
    font-size: 13px;
    line-height: 17px;
    color: var(--ink);
  }
  .contact li { display: flex; align-items: center; gap: 6px; }
  .contact svg { width: 10px; height: 10px; fill: var(--navy); flex: none; }
  .contact .address { display: block; margin-top: 2px; }

  .brand { display: flex; align-items: center; gap: 10px; }
  .brand__dot { width: 34px; height: 34px; border-radius: 50%; flex: none; }
  .brand__name {
    font-weight: 900;
    text-transform: uppercase;
    line-height: .95;
    letter-spacing: 1px;
  }
  .card--front .brand {
    position: absolute;
    left: 262px;
    top: 104px;
  }
  .card--front .brand__dot { border: 3px solid var(--navy); }
  .card--front .brand__name { color: var(--navy); font-size: 25px; }
  .card--back .brand__dot { border: 3px solid var(--paper); width: 42px; height: 42px; }
  .card--back .brand__name { color: var(--paper); font-size: 30px; }

  .footer-rule {
    position: absolute;
    left: 0;
    right: 0;
    bottom: 62px;
    height: 4px;
    background: var(--gray);
  }
  .footer-band {
    position: absolute;
    left: 0;
    right: 0;
    bottom: 0;
    height: 54px;
    background: var(--navy);
  }
</style>
</head>
<body>
  <article class="card card--front">
    <div class="holder">
      <p class="holder__name">Daniel Harlow</p>
      <p class="holder__role">Managing Director</p>
    </div>
    <ul class="contact">
      <li><svg viewBox="0 0 10 10"><path d="M2 0h2l1 3-1.5 1a6 6 0 0 0 2.5 2.5L7 5l3 1v2c0 1-1 2-2 2A8 8 0 0 1 0 2c0-1 1-2 2-2z"/></svg>044-987 654 321</li>
      <li><svg viewBox="0 0 10 10"><path d="M0 2h10v6H0z M0 2l5 3.5L10 2" stroke="#fff" stroke-width=".8"/></svg>hello@brightkeel.com</li>
      <li><svg viewBox="0 0 10 10"><circle cx="5" cy="5" r="5"/></svg>www.brightkeel.com</li>
      <li class="address">12345, Address Goes Here<br>Country Name, 123456</li>
    </ul>
    <div class="brand">
      <span class="brand__dot"></span>
      <span class="brand__name">Brightkeel<br>Logistics</span>
    </div>
    <div class="footer-rule" aria-hidden="true"></div>
    <div class="footer-band" aria-hidden="true"></div>
  </article>

  <article class="card card--back">
    <div class="brand">
      <span class="brand__dot"></span>
      <span class="brand__name">Brightkeel<br>Logistics</span>
    </div>
  </article>
</body>
</html>
```